Tri-Fold Brochure for Substance Abuse Recovery Center

We are looking to freshen up our tri-fold brochure for our recovery facility. Something that helps convey our message of treatment in the great outdoors. I've included a word document with a mock up.

```html
<!DOCTYPE html>
<html lang="en">
<head>
<meta charset="utf-8">
<title>Silver Pine Ridge Recovery Center – Brochure Inside</title>
<link rel="stylesheet" href="https://fonts.googleapis.com/css2?family=Roboto+Slab:wght@300;400;600&family=Lato:ital,wght@1,300&display=swap">
<style>
  :root {
    --sky-top: #c6e6f7;
    --sky-bottom: #e4f3fb;
    --heading: #2b7aa6;
    --body: #3f8fba;
    --rule: #6aa8cc;
    --panel-text: #ffffff;
    --band: #1b6b93;
    --quote-box: #3b86ae;
    --quote-tint: #8bbcd8;
  }
  * { margin: 0; padding: 0; box-sizing: border-box; }
  html, body { width: 1200px; height: 930px; overflow: hidden; }
  body {
    position: relative;
    font-family: "Roboto Slab", Rockwell, "Courier New", serif;
    background: linear-gradient(180deg, var(--sky-top) 0%, var(--sky-bottom) 75%, #f3f9fd 100%);
  }
  .brochure { position: absolute; inset: 0; width: 1200px; height: 930px; }

  .hero-photo {
    position: absolute; left: 130px; top: 540px; width: 670px; height: 363px;
    background: radial-gradient(ellipse at 60% 65%, #f2e4da 0%, #eef4f8 40%, rgba(228,243,251,0) 72%);
  }

  .section { position: absolute; }
  .section h2 {
    font-weight: 600; color: var(--heading);
    font-size: 29px; line-height: 36px;
    padding-bottom: 8px;
    border-bottom: 2px dotted var(--rule);
    margin-bottom: 10px;
  }
  .section p {
    font-weight: 300; color: var(--body);
    font-size: 15px; line-height: 19.2px;
    margin-bottom: 5px;
  }

  .who { left: 28px; top: 106px; width: 344px; }
  .philosophy { left: 28px; top: 370px; width: 344px; }
  .relapse { left: 430px; top: 42px; width: 342px; }
  .improvement { left: 430px; top: 372px; width: 342px; }

  .brand {
    position: absolute; left: 232px; top: 58px; width: 140px;
    color: var(--heading); font-weight: 600; font-size: 14px; line-height: 17px;
    text-align: right;
  }

  .quote-box { position: absolute; left: 32px; top: 650px; width: 334px; height: 253px; }
  .quote {
    position: absolute; left: 50px; top: 752px; width: 300px;
    font-family: "Lato", Arial, sans-serif; font-style: italic; font-weight: 300;
    color: #ffffff; font-size: 17px; line-height: 20px;
  }
  .quote cite {
    display: block; text-align: right; font-style: normal; margin-top: 6px;
    font-family: "Roboto Slab", Rockwell, serif; font-weight: 300; font-size: 16px;
  }

  .side-panel { position: absolute; left: 800px; top: 0; width: 400px; height: 903px; }
  .side-section { position: absolute; left: 848px; width: 318px; color: var(--panel-text); }
  .side-section h2 {
    font-weight: 600; font-size: 29px; line-height: 36px;
    padding-bottom: 8px; border-bottom: 2px dotted rgba(255,255,255,0.75);
    margin-bottom: 10px;
  }
  .side-section ul { list-style: none; }
  .side-section li { position: relative; padding-left: 26px; font-weight: 400; }
  .side-section li::before {
    content: ""; position: absolute; left: 2px; top: 7px;
    border-left: 11px solid transparent; border-bottom: 11px solid #ffffff;
  }
  .program { top: 50px; }
  .program li { font-size: 16.5px; line-height: 21px; margin-bottom: 7.6px; }
  .program li.wrap { padding-left: 0; text-indent: 26px; }
  .activities { top: 398px; }
  .activities li { font-size: 15.5px; line-height: 20px; margin-bottom: 7.7px; text-transform: uppercase; }

  .footer-band { position: absolute; left: 0; top: 903px; width: 1200px; height: 27px; background: var(--band); }
</style>
</head>
<body>
<div class="brochure">

  <div class="hero-photo" role="img" aria-label="Photo of a joyful young woman with arms spread wide against a bright open sky"></div>

  <svg class="side-panel" viewBox="0 0 400 903" aria-hidden="true">
    <defs>
      <linearGradient id="panelFill" x1="0" y1="0" x2="0" y2="1">
        <stop offset="0" stop-color="#4a9ecf"/>
        <stop offset="0.45" stop-color="#67acd6"/>
        <stop offset="1" stop-color="#aacbe1"/>
      </linearGradient>
    </defs>
    <rect width="400" height="903" fill="url(#panelFill)"/>
    <polygon points="0,0 400,0 400,40 0,0" fill="#ffffff" opacity="0.18"/>
    <polygon points="0,290 400,400 400,903 0,903" fill="#ffffff" opacity="0.12"/>
    <polygon points="0,380 400,250 400,903 0,903" fill="#ffffff" opacity="0.08"/>
    <polygon points="0,290 230,350 0,380" fill="#ffffff" opacity="0.10"/>
  </svg>

  <div class="brand">Silver Pine Ridge Recovery Center</div>

  <section class="section who">
    <h2>Who We Are</h2>
    <p>We are a team with a passion for recovery. We are advocates that care about helping find people the right fit for them...even if it isn’t with Silver Pine Ridge.</p>
    <p>However, we feel that Silver Pine Ridge is the destination recovery center. It allows individuals personal treatment plans, and an unmatched environment.</p>
  </section>

  <section class="section philosophy">
    <h2>Our Philosophy</h2>
    <p>At Silver Pine Ridge, we focus on individualized treatment plans to address mental health, medical and emotional needs. We incorporate the Relapse Prevention Program and treat trauma and co-occurring disorders.</p>
  </section>

  <section class="section relapse">
    <h2>Relapse Prevention Program</h2>
    <p>We know the statistics. We want them to change.</p>
    <p>Our Relapse Prevention Program offers an intensive 2 week stabilization program for clients.</p>
    <p>If a patient has been to treatment before, this is the program for them. Our programs have traditional steps to them, with unique individual therapies and recovery options.</p>
  </section>

  <section class="section improvement">
    <h2>Improvement</h2>
    <p>We want EVERYONE to walk out of our facility an improved individual. This includes helping improve credit scores, interviewing skills and family foundations.</p>
    <p>Clients learn to reshape their lives with healthy coping skills.</p>
    <p>Our HOPE Program offers Heart Centered Healing: Emotionally Focused Therapy</p>
  </section>

  <svg class="quote-box" viewBox="0 0 334 253" aria-hidden="true">
    <polygon points="0,0 334,70 334,253 0,253" fill="var(--quote-box)"/>
    <polygon points="0,0 334,70 334,100" fill="var(--quote-tint)" opacity="0.85"/>
  </svg>
  <blockquote class="quote">
    “Silver Pine Ridge is not your typical center. Patients don’t just sit around all day. There are so many activities that keep them engaged and working on themselves.”
    <cite>-Marisa T.</cite>
  </blockquote>

  <section class="side-section program">
    <h2>Our Program</h2>
    <ul>
      <li class="wrap">A 30 Day Residential Inpatient &amp; Outpatient Treatment.</li>
      <li>Ongoing Recovery Care</li>
      <li>Dialectical Behavioral Therapy</li>
      <li>Emotionally Focused Therapy</li>
      <li>Solution Focused Therapy</li>
      <li>Adventure Therapy</li>
    </ul>
  </section>

  <section class="side-section activities">
    <h2>Activities</h2>
    <ul>
      <li>Bio Bed</li>
      <li>Acupuncture</li>
      <li>Weekly In-House Salon</li>
      <li>Kayaking</li>
      <li>Hiking</li>
      <li>Fire Pits</li>
      <li>Biking</li>
      <li>Yoga</li>
      <li>Fitness Center</li>
      <li>Pool</li>
      <li>Navigation Ropes Courses</li>
      <li>Zip-Lining</li>
      <li>Rock Climbing</li>
      <li>Games</li>
      <li>Fishing</li>
    </ul>
  </section>

  <div class="footer-band"></div>
</div>
</body>
</html>
```